Business Card Design

I already have a company logo for my company. I have a logo for the manufacturer we represent. I want a professional business card design.

```html
<!DOCTYPE html>
<html lang="en">
<head>
<meta charset="UTF-8">
<title>Signal Guard Co. — Business Card</title>
<link rel="stylesheet" href="https://fonts.googleapis.com/css2?family=Montserrat:wght@400;500;700;800&display=swap">
<style>
  :root {
    --stage: #3b3633;
    --card-white: #ffffff;
    --card-black: #161616;
    --accent-red: #e0252b;
    --ink: #1d1d1d;
    --ink-soft: #333333;
    --logo-light: #cfcfcf;
  }
  * { box-sizing: border-box; margin: 0; padding: 0; }
  html, body {
    width: 1200px; height: 786px; overflow: hidden;
    background: var(--stage);
    font-family: "Montserrat", Arial, sans-serif;
  }
  .stage {
    position: relative; width: 1200px; height: 786px;
    display: flex; align-items: center; justify-content: center; gap: 48px;
  }
  .card {
    position: relative; width: 540px; height: 309px;
    border-radius: 3px;
    box-shadow: 0 14px 30px rgba(0,0,0,0.45);
  }
  .card--front { background: var(--card-white); color: var(--ink); }
  .card--back { background: var(--card-black); display: flex; align-items: center; justify-content: center; }

  .brand {
    display: flex; align-items: center; gap: 10px;
    font-weight: 800; font-size: 24px; letter-spacing: 0.5px;
    text-transform: uppercase;
  }
  .brand__dot { width: 14px; height: 14px; border-radius: 50%; background: var(--accent-red); }
  .card--front .brand { position: absolute; top: 58px; right: 40px; color: var(--accent-red); }
  .card--back .brand { color: var(--logo-light); font-size: 28px; }

  .person { position: absolute; left: 34px; top: 142px; }
  .person__name { color: var(--accent-red); font-weight: 700; font-size: 22px; line-height: 1.1; }
  .person__title { font-size: 12.5px; font-weight: 500; color: var(--ink-soft); margin-top: 2px; }

  .divider {
    position: absolute; left: 34px; right: 56px; top: 190px;
    height: 1.5px; background: var(--accent-red);
  }

  .address {
    position: absolute; right: 40px; top: 204px;
    font-size: 11.5px; line-height: 1.35; color: var(--ink); text-align: left;
  }

  .contacts { position: absolute; left: 34px; top: 214px; list-style: none; }
  .contacts li {
    display: flex; align-items: center; gap: 12px;
    font-size: 12.5px; line-height: 1; color: var(--ink); margin-bottom: 9px;
  }
  .contacts svg { width: 11px; height: 11px; flex: none; fill: var(--accent-red); }
</style>
</head>
<body>
<main class="stage">
  <section class="card card--front" aria-label="Business card front">
    <div class="brand"><span class="brand__dot"></span>Signal Guard Co.</div>

    <div class="person">
      <p class="person__name">Daniel Reyes</p>
      <p class="person__title">Managing Director</p>
    </div>

    <div class="divider"></div>

    <address class="address">240 Harlow Ave<br>Brookfield, CO 80231</address>

    <ul class="contacts">
      <li>
        <svg viewBox="0 0 12 12" aria-hidden="true"><path d="M2 1h2.5l1 3-1.5 1a6 6 0 0 0 3 3l1-1.5 3 1V11a1 1 0 0 1-1 1A10 10 0 0 1 0 2a1 1 0 0 1 1-1z"/></svg>
        555.210.0187
      </li>
      <li>
        <svg viewBox="0 0 12 12" aria-hidden="true"><path d="M0 2h12v8H0z M0 2l6 4.5L12 2" stroke="#fff" stroke-width="1"/></svg>
        info@signalguardco.com
      </li>
      <li>
        <svg viewBox="0 0 12 12" aria-hidden="true"><circle cx="6" cy="6" r="6"/><path d="M0 6h12M6 0v12M6 0c-3 3-3 9 0 12M6 0c3 3 3 9 0 12" stroke="#fff" stroke-width="0.8" fill="none"/></svg>
        www.signalguardco.com
      </li>
    </ul>
  </section>

  <section class="card card--back" aria-label="Business card back">
    <div class="brand"><span class="brand__dot"></span>Signal Guard Co.</div>
  </section>
</main>
</body>
</html>
```